Submittal Letter - Letterhead

want something that matches our colors that looks professional for a design build engineering fan. Feel Free to incorporate Engineering, Procurement, Construction and Maintenance as a tagline type heading if it makes sense.

```html
<!DOCTYPE html>
<html lang="en">
<head>
<meta charset="utf-8">
<title>Harlan Brooks Letterhead</title>
<link href="https://fonts.googleapis.com/css2?family=Lato:wght@400;700&family=Montserrat:wght@400;500&family=Niconne&display=swap" rel="stylesheet">
<style>
  :root {
    --bg: #dcdcdc;
    --paper: #ffffff;
    --ink: #1d1d1d;
    --ink-soft: #333333;
    --brand-red: #d7282f;
  }
  * { margin: 0; padding: 0; box-sizing: border-box; }
  html, body { width: 1153px; height: 1200px; overflow: hidden; background: var(--bg); }
  .letterhead {
    position: absolute; left: 252px; top: 181px;
    width: 648px; height: 838px; background: var(--paper);
    font-family: "Lato", sans-serif; color: var(--ink);
  }
  .brand {
    position: absolute; left: 40px; top: 72px;
    display: flex; align-items: center; gap: 8px;
    font-family: "Montserrat", sans-serif; font-weight: 500;
    font-size: 17px; color: var(--ink);
  }
  .brand-dot { width: 26px; height: 26px; border-radius: 50%; background: var(--brand-red); }
  .company {
    position: absolute; right: 185px; top: 66px; text-align: right;
    font-family: "Montserrat", sans-serif; font-size: 11.2px; line-height: 15.5px; color: var(--ink-soft);
  }
  .company-name { font-size: 13px; font-weight: 500; color: var(--ink); }
  .divider { position: absolute; left: 479px; top: 68px; width: 1.5px; height: 43px; background: var(--brand-red); }
  .contacts {
    position: absolute; left: 498px; top: 73px;
    font-family: "Montserrat", sans-serif; font-size: 11.2px; line-height: 16px; color: var(--ink-soft);
  }
  .contacts li { list-style: none; display: flex; align-items: center; gap: 6px; }
  .contacts svg { width: 9px; height: 9px; }
  .tagline {
    position: absolute; left: 40px; top: 157px; width: 568px;
    font-family: "Montserrat", sans-serif; font-size: 13.6px; color: var(--ink-soft);
    white-space: nowrap;
  }
  .rule { position: absolute; left: 40px; top: 183px; width: 568px; height: 1.2px; background: var(--brand-red); }
  .body { position: absolute; left: 40px; top: 222px; width: 568px; font-size: 13.3px; line-height: 14.6px; }
  .date { margin-bottom: 16px; }
  .recipient { margin-bottom: 14px; }
  .address { margin-bottom: 14px; }
  .salutation { font-weight: 700; font-size: 16.5px; margin-bottom: 14px; }
  .body p.para { text-align: justify; margin-bottom: 13px; }
  .closing { margin-top: 26px; }
  .signature {
    position: absolute; left: 40px; top: 726px;
    font-family: "Niconne", cursive; font-size: 31px; color: var(--ink);
  }
</style>
</head>
<body>
<main class="letterhead">
  <div class="brand"><span class="brand-dot"></span>Harlan Brooks</div>

  <div class="company">
    <div class="company-name">Harlan Brooks, Inc. (HBI)</div>
    <div>4470 Meridian Avenue</div>
    <div>Fairview, CA 90000</div>
  </div>
  <div class="divider"></div>
  <ul class="contacts">
    <li><svg viewBox="0 0 10 10"><path d="M2 1 L4 1 L4.6 3.2 L3.4 4 Q4.4 6 6 6.6 L6.8 5.4 L9 6 L9 8 Q9 9 8 9 Q1 8.5 1 2 Q1 1 2 1 Z" fill="var(--brand-red)"/></svg>(800) 555-0148</li>
    <li><svg viewBox="0 0 10 10"><circle cx="5" cy="5" r="4.5" fill="var(--brand-red)"/><path d="M1 5 H9 M5 0.5 Q2.5 5 5 9.5 M5 0.5 Q7.5 5 5 9.5" stroke="#fff" stroke-width="0.8" fill="none"/></svg>www.hbinc.com</li>
  </ul>

  <div class="tagline">Feel Free to incorporate Engineering, Procurement, Construction and Maintenance</div>
  <div class="rule"></div>

  <section class="body">
    <p class="date">January-03-2020</p>
    <p class="recipient">Mr, John Doe<br>President</p>
    <p class="address">Link Corppration<br>123 Street Name, Suite# 10<br>City, State, 120023</p>
    <p class="salutation">Dear Mr, John</p>
    <p class="para">Lorem ipsum dolor sit amet, consectetur adipiscing elit, sed do eiusmod tempor incididunt ut labore et dolore magna aliqua. Ut enim ad minim veniam, quis nostrud exercitation ullamco laboris nisi ut aliquip ex ea commodo consequat. Duis aute irure dolor in reprehenderit in voluptate velit esse cillum dolore eu fugiat nulla pariatur.</p>
    <p class="para">Lorem ipsum dolor sit amet, consectetur adipiscing elit, sed do eiusmod tempor incididunt ut labore et dolore magna aliqua. Ut enim ad minim veniam, quis nostrud exercitation ullamco laboris nisi ut aliquip ex ea commodo consequat. Duis aute irure dolor in reprehenderit in voluptate velit esse cillum dolore eu fugiat nulla pariatur.</p>
    <p class="para">Lorem ipsum dolor sit amet, consectetur adipiscing elit, sed do eiusmod tempor incididunt ut labore et dolore magna aliqua. Ut enim ad minim veniam, quis nostrud exercitation ullamco laboris nisi ut aliquip ex ea commodo consequat.</p>
    <p class="para">Excepteur sint occaecat cupidatat non proident, sunt in culpa qui officia deserunt mollit anim id est laborum. re et dolore magnam aliquam quaerat voluptatem.</p>
    <p class="closing">Regards</p>
  </section>

  <div class="signature">Daniel Reeve</div>
</main>
</body>
</html>
```